Flyer Design

STERLING SHADES
ph:9361 4085
7/41 Pellow Street
Malaga, WA 6069
we need a flyer design for a part broshure part flyer asking for business. well astablished small business for 15years. we manufacture blinds to domestic and commercial. custom made and premium quality. very competitive, free measure and quote even on weekend, plus we offer free fitting to all area. can supply all type of blinds as in big companies. such as roller blinds, roman blinds, timber venetians, slimline venetians, panel glide, vertical blinds, timber shutters etc.

Target Market(s)

new home

Industry/Entity Type

Small Business

Requirements
Nice to have
• a few different type of blinds in partially or part of it may be...

```html
<!DOCTYPE html>
<html lang="en">
<head>
<meta charset="utf-8">
<title>Sterling Shades Flyer</title>
<link href="https://fonts.googleapis.com/css2?family=Encode+Sans+Condensed:wght@300&family=PT+Sans:wght@700&family=PT+Sans+Narrow:wght@400;700&display=swap" rel="stylesheet">
<style>
  :root {
    --page-bg: #1b1b1b;
    --gold-dark: #7d5e1c;
    --gold-mid: #98732a;
    --gold-light: #a97c35;
    --cream: #fbf1d8;
    --white: #ffffff;
    --ink: #3a2f1c;
    --band: rgba(40, 30, 15, 0.72);
    --rule: rgba(255, 240, 210, 0.55);
    --frame: #f7f5f0;
  }
  * { margin: 0; padding: 0; box-sizing: border-box; }
  html, body { width: 1200px; height: 1200px; overflow: hidden; background: var(--page-bg); }
  body { font-family: "PT Sans Narrow", "Arial Narrow", sans-serif; color: var(--white); }

  .flyer {
    position: absolute; left: 230px; top: 97px; width: 835px; height: 1028px;
    background: linear-gradient(160deg, var(--gold-mid) 0%, var(--gold-dark) 35%, var(--gold-light) 75%, var(--gold-mid) 100%);
    overflow: hidden;
  }

  .brand {
    position: absolute; top: 52px; left: 0; width: 805px; text-align: center;
    font-size: 82px; line-height: 1; color: var(--cream); letter-spacing: 1px; white-space: nowrap;
  }
  .brand-light { font-family: "Encode Sans Condensed", sans-serif; font-weight: 300; }
  .brand-bold { font-family: "PT Sans", sans-serif; font-weight: 700; }

  .since {
    position: absolute; top: 156px; left: 0; width: 805px; text-align: center;
    font-size: 31px; line-height: 40px; color: var(--cream);
  }
  .since::before, .since::after {
    content: ""; display: inline-block; width: 150px; height: 4px; vertical-align: middle;
    border-top: 1px solid var(--rule); border-bottom: 1px solid var(--rule); margin: 0 18px;
  }

  .tagline {
    position: absolute; top: 225px; left: 0; width: 835px; text-align: center;
    font-size: 31px; line-height: 60px;
  }
  .drop { font-weight: 700; font-size: 46px; }

  .window-photo {
    position: absolute; left: 38px; top: 308px; width: 449px; height: 547px;
    background: linear-gradient(180deg, #f4f2ee 0%, #ffffff 40%, #e9e6e0 80%, #6a6258 100%);
    border: 10px solid var(--frame);
  }
  .call-icon { position: absolute; left: 170px; top: 470px; width: 115px; height: 115px; }
  .call-number {
    position: absolute; left: 38px; top: 595px; width: 420px; text-align: center;
    font-size: 46px; line-height: 56px; font-weight: 700; letter-spacing: 4px; color: var(--ink);
  }

  .point { position: absolute; left: 513px; width: 300px; white-space: nowrap; }
  .point .big { font-size: 50px; }
  .point .lead { font-weight: 700; font-size: 50px; }
  .point.quality { top: 328px; font-size: 30px; line-height: 44px; }
  .point.competitive { top: 460px; font-size: 48px; line-height: 45px; }
  .point.free { top: 600px; font-size: 28px; line-height: 32px; }
  .point.free .first-line { display: block; line-height: 46px; }
  .point.supply { top: 774px; font-size: 25px; line-height: 38px; }
  .point.supply .lead { font-size: 46px; }

  .range {
    position: absolute; left: 38px; top: 866px; width: 780px; list-style: none;
    display: grid; grid-template-columns: 161px 175px 205px auto; row-gap: 8px;
    font-size: 25px; line-height: 31px; white-space: nowrap;
  }
  .range li::before {
    content: ""; display: inline-block; width: 19px; height: 19px; border-radius: 50%;
    background: var(--white); margin-right: 10px; vertical-align: -1px;
  }
  .range .wide { grid-column: span 2; }

  .contact-band {
    position: absolute; left: 0; bottom: 0; width: 835px; height: 84px; background: var(--band);
    display: flex; align-items: center; padding-left: 36px;
    font-weight: 700; font-size: 20px; color: var(--cream); letter-spacing: 0.3px; white-space: nowrap;
  }
  .contact-band svg { margin-right: 12px; }
  .contact-phone { margin-left: 44px; display: flex; align-items: center; letter-spacing: 3px; }
</style>
</head>
<body>
  <main class="flyer">
    <h1 class="brand"><span class="brand-light">STERLING</span> <span class="brand-bold">SHADES</span></h1>
    <p class="since">Since 15 Years</p>
    <p class="tagline"><span class="drop">W</span>e manufacture blinds to domestic and commercial.</p>

    <div class="window-photo" role="img" aria-label="Bright window with white venetian blinds and potted violets on the sill"></div>
    <svg class="call-icon" viewBox="0 0 100 100" aria-hidden="true">
      <path d="M14 10 C30 0 44 14 40 30 L32 40 C40 58 52 70 64 76 L74 66 C88 62 98 78 88 90 C60 104 4 58 14 10 Z" fill="#5a4a30"/>
      <path d="M84 92 q6 6 12 0" stroke="#5a4a30" stroke-width="3" fill="none"/>
    </svg>
    <p class="call-number">9361 4085</p>

    <p class="point quality">Custom made and<br>premium <span class="big">quality</span>.</p>
    <p class="point competitive"><span class="lead">V</span>ery<br>competitive,</p>
    <p class="point free"><span class="first-line"><span class="big">FREE</span> measure and</span>quote even on weekend,<br>plus we offer free fitting<br>to all area.</p>
    <p class="point supply"><span class="lead">C</span>an supply all type of<br>blinds as in big companies.</p>

    <ul class="range">
      <li>Roller blinds</li>
      <li>Roman blinds</li>
      <li>Timber venetians</li>
      <li>Slimline venetians</li>
      <li>Panel glide</li>
      <li>Vertical blinds</li>
      <li class="wide">Timber shutters and many more....</li>
    </ul>

    <footer class="contact-band">
      <svg width="24" height="18" viewBox="0 0 24 18" aria-hidden="true">
        <rect x="1" y="1" width="22" height="16" fill="none" stroke="#fbf1d8" stroke-width="2"/>
        <path d="M1 1 L12 10 L23 1 M1 17 L9 8 M23 17 L15 8" stroke="#fbf1d8" stroke-width="2" fill="none"/>
      </svg>
      <span>STERLING SHADES&nbsp; 7/41 PELLOW STREET MALAGA, WA 6069</span>
      <span class="contact-phone">
        <svg width="34" height="34" viewBox="0 0 100 100" aria-hidden="true">
          <path d="M14 10 C30 0 44 14 40 30 L32 40 C40 58 52 70 64 76 L74 66 C88 62 98 78 88 90 C60 104 4 58 14 10 Z" fill="#c9b58a"/>
        </svg>
        9361 4085
      </span>
    </footer>
  </main>
</body>
</html>
```